Website design for an Italian restaurant in Amsterdam

I need a design for a client of mine. It is for Teatro Lunaverde, an Italian restaurant in Amsterdam.
We are going for a clean, modern look but we also need to realise an authentic feel.
The restaurant is located in an old movie theatre, that is where the name Teatro Lunaverde comes from.
Industry/Entity Type
Italian Restaurant
Number of Pages Required
1 page
Font styles to use
Sans Serif
Colors
Designer to choose colors to be used in the design.

```html
<!DOCTYPE html>
<html lang="en">
<head>
<meta charset="utf-8">
<title>Teatro Lunaverde – Italian Restaurant</title>
<link href="https://fonts.googleapis.com/css2?family=Exo+2:wght@400;500;600&family=Lato:wght@400;700&display=swap" rel="stylesheet">
<style>
:root{
  --black:#060606;
  --panel:#1c1c1c;
  --footer:#161616;
  --purple:#4c4296;
  --purple-light:#5a4fb0;
  --white:#ffffff;
  --muted:#cfcfcf;
  --red:#c0262d;
  --line:#9a9a9a;
}
*{box-sizing:border-box;margin:0;padding:0}
html,body{width:1200px;height:3409px;overflow:hidden}
body{background:var(--black);color:var(--white);font-family:"Lato",Arial,sans-serif;position:relative}
.abs{position:absolute}
.display{font-family:"Exo 2",Arial,sans-serif;font-weight:500;letter-spacing:1px}
.btn{position:absolute;border:2px solid var(--white);border-radius:18px;color:var(--white);font-size:13px;display:flex;align-items:center;justify-content:center;height:34px}
.btn.filled{background:var(--purple);border-color:var(--purple)}
.section-title{position:absolute;left:0;width:1200px;text-align:center;font-size:38px}
.title-rule{position:absolute;left:545px;width:110px;height:4px;background:var(--purple)}

/* hero */
.hero{top:0;left:0;width:1200px;height:705px;background:radial-gradient(ellipse at 60% 40%,#6b5438 0%,#3a2c1e 40%,#140f0b 100%)}
.menu-toggle{left:72px;top:38px;width:46px;height:46px}
.brand{top:40px;left:0;width:1200px;text-align:center;font-size:34px}
.hero-kicker{top:296px;left:0;width:1200px;text-align:center;font-size:36px}
.hero-title{top:346px;left:0;width:1200px;text-align:center;font-size:64px}
.dots{top:434px;left:570px;display:flex;gap:8px}
.dots span{width:12px;height:12px;border-radius:50%;border:2px solid var(--white)}
.dots span.on{background:var(--purple-light);border-color:var(--purple-light)}

/* menu */
.menu{top:705px;left:0;width:1200px;height:740px;background:linear-gradient(180deg,#111 0%,#050505 100%)}
.dish{position:absolute;width:260px;text-align:center}
.dish-photo{width:190px;height:120px;margin:0 auto;border-radius:50%}
.dish h3{font-size:24px;margin-top:68px}
.dish p{font-size:12px;line-height:15px;margin:10px auto 0;width:200px}
.arrow{position:absolute;width:30px;height:56px}

/* offer */
.offer{top:1445px;left:0;width:1200px;height:495px}
.offer-panel{position:absolute;left:0;top:0;width:630px;height:495px;background:var(--panel)}
.offer h2{position:absolute;left:191px;top:48px;font-size:38px;line-height:48px;font-weight:500}
.offer-rule{position:absolute;left:191px;top:218px;width:339px;height:4px;background:var(--purple)}
.offer p{position:absolute;left:191px;top:277px;width:395px;font-size:12px;line-height:15px}
.offer-photo{position:absolute;left:630px;top:0;width:570px;height:495px;background:linear-gradient(160deg,#5a4a3a 0%,#2a2019 55%,#120e0b 100%)}

/* blogs */
.blogs{top:1940px;left:0;width:1200px;height:760px;background:#050505}
.card{position:absolute;top:199px;width:266px;height:327px;background:var(--white);border-radius:8px;overflow:hidden;color:#222}
.card-photo{height:170px}
.card h4{font-family:"Exo 2",Arial,sans-serif;font-weight:500;font-size:18px;margin:28px 0 0 20px}
.card-meta{display:flex;gap:40px;font-size:10px;margin:12px 20px 0;color:#444}
.card p{font-size:11px;line-height:14px;margin:8px 20px 0;color:#444}
.card .more{font-size:10px;font-weight:700;margin:10px 20px 0;display:block}
.card .more.hot{color:var(--red)}

/* contact */
.contact{top:2650px;left:0;width:1200px;height:489px;background:#0a0a0a}
.map-shape{position:absolute;left:270px;top:110px;width:660px;height:370px;border-radius:40%;background:radial-gradient(ellipse,#1e1e1e 0%,#0a0a0a 70%)}
.field{position:absolute;left:391px;width:416px;border-bottom:2px solid var(--line);font-size:13px;padding-bottom:8px}

/* footer */
.footer{top:3139px;left:0;width:1200px;height:270px;background:var(--footer)}
.footer h5{position:absolute;font-family:"Exo 2",Arial,sans-serif;color:var(--purple-light);font-weight:600;font-size:14px;letter-spacing:.5px}
.footer .txt{position:absolute;font-size:11px;line-height:15px}
.socials{position:absolute;left:195px;top:157px;display:flex;gap:10px}
.socials span{width:16px;height:16px;border-radius:50%;background:var(--purple)}
.contact-row{position:absolute;left:609px;display:flex;gap:14px;font-size:11px;line-height:15px}
.subscribe{position:absolute;left:807px;top:138px;width:210px;height:28px;background:var(--white);font-size:11px;color:#999;padding:8px 8px}
.subscribe-go{position:absolute;left:968px;top:138px;width:49px;height:28px;background:var(--purple)}
.foot-rule{position:absolute;left:195px;top:202px;width:822px;height:1px;background:#555}
.legal{position:absolute;top:215px;font-size:11px}
</style>
</head>
<body>

<section class="hero abs" role="img" aria-label="Dim restaurant dining room inside a former cinema, warm bulb lights and set tables">
  <svg class="menu-toggle abs" viewBox="0 0 46 46"><circle cx="23" cy="23" r="21" fill="none" stroke="#fff" stroke-width="3"/><rect x="13" y="15" width="20" height="3" fill="#fff"/><rect x="13" y="22" width="20" height="3" fill="#fff"/><rect x="13" y="29" width="20" height="3" fill="#fff"/></svg>
  <div class="brand abs display">TEATRO LUNAVERDE</div>
  <div class="hero-kicker abs display">WELCOME TO</div>
  <h1 class="hero-title abs display">ITALIAN RESTURENT</h1>
  <div class="dots abs"><span class="on"></span><span></span><span></span></div>
  <a class="btn" style="left:534px;top:497px;width:136px">Read More</a>
</section>

<section class="menu abs">
  <h2 class="section-title display" style="top:52px">MENU</h2>
  <div class="title-rule" style="top:111px"></div>
  <svg class="arrow" style="left:82px;top:244px" viewBox="0 0 30 56"><path d="M26 4 4 28l22 24" fill="none" stroke="#888" stroke-width="3"/></svg>
  <svg class="arrow" style="left:1080px;top:244px" viewBox="0 0 30 56"><path d="M4 4l22 24L4 52" fill="none" stroke="#5a4fb0" stroke-width="3"/></svg>
  <div class="dish" style="left:166px;top:200px">
    <div class="dish-photo" role="img" aria-label="Pepperoni pizza" style="background:radial-gradient(ellipse,#c0502a 0%,#8a3a1e 70%)"></div>
    <h3 class="display">PIZZA</h3>
    <p>Lorem Ipsum is simply dummy text of the printing and typesetting industry.</p>
    <a class="btn" style="left:62px;top:267px;width:136px">Detail</a>
  </div>
  <div class="dish" style="left:470px;top:200px">
    <div class="dish-photo" role="img" aria-label="Plate of spaghetti with tomato sauce and basil" style="background:radial-gradient(ellipse,#d8472a 0%,#e9d9c0 45%,#f4f4f4 70%)"></div>
    <h3 class="display">PASTA</h3>
    <p>Lorem Ipsum is simply dummy text of the printing and typesetting industry.</p>
    <a class="btn filled" style="left:62px;top:267px;width:136px">Detail</a>
  </div>
  <div class="dish" style="left:776px;top:200px">
    <div class="dish-photo" role="img" aria-label="Slice of lasagna on a white plate" style="background:radial-gradient(ellipse,#c98a3e 0%,#e7cfa2 45%,#f2f2f2 70%)"></div>
    <h3 class="display">LASAGNA</h3>
    <p>Lorem Ipsum is simply dummy text of the printing and typesetting industry.</p>
    <a class="btn" style="left:62px;top:267px;width:136px">Detail</a>
  </div>
  <a class="btn" style="left:532px;top:628px;width:136px">View All Menu</a>
</section>

<section class="offer abs">
  <div class="offer-panel">
    <h2 class="display">WE OFFER THE<br>BEST MEAL AT THE<br>BEST VALUE</h2>
    <div class="offer-rule"></div>
    <p>Lorem Ipsum is simply dummy text of the printing and typesetting industry. Lorem Ipsum has been the industry's standard dummy text ever since the 1500s, when an unknown printer took a galley of type and scrambled it to make a type specimen book.</p>
    <a class="btn" style="left:196px;top:400px;width:136px">Book a Table</a>
  </div>
  <div class="offer-photo" role="img" aria-label="Restaurant hall with chandelier, tables and a large screen"></div>
</section>

<section class="blogs abs">
  <h2 class="section-title display" style="top:70px">BLOGS</h2>
  <div class="title-rule" style="top:128px"></div>
  <svg class="arrow" style="left:82px;top:334px" viewBox="0 0 30 56"><path d="M26 4 4 28l22 24" fill="none" stroke="#888" stroke-width="3"/></svg>
  <svg class="arrow" style="left:1080px;top:334px" viewBox="0 0 30 56"><path d="M4 4l22 24L4 52" fill="none" stroke="#5a4fb0" stroke-width="3"/></svg>
  <article class="card" style="left:188px">
    <div class="card-photo" role="img" aria-label="Fresh salad bowls on a wooden table" style="background:linear-gradient(135deg,#6b4a2a,#7fa34a 60%,#e9e4d8)"></div>
    <h4>BLOG 1</h4>
    <div class="card-meta"><span>▦ 19.6.2018</span><span>▢ 12 Comments</span></div>
    <p>Lorem Ipsum is simply dummy text of the printing and typesetting industry.</p>
    <span class="more hot">READ MORE..</span>
  </article>
  <article class="card" style="left:466px">
    <div class="card-photo" role="img" aria-label="Spaghetti with meatballs" style="background:radial-gradient(ellipse,#a0381e 0%,#d9a253 50%,#3a2a20 100%)"></div>
    <h4>BLOG 2</h4>
    <div class="card-meta"><span>▦ 19.6.2018</span><span>▢ 12 Comments</span></div>
    <p>Lorem Ipsum is simply dummy text of the printing and typesetting industry.</p>
    <span class="more">READ MORE..</span>
  </article>
  <article class="card" style="left:745px">
    <div class="card-photo" role="img" aria-label="Table of shared Italian dishes seen from above" style="background:linear-gradient(135deg,#5c3a24,#c96a3a 50%,#e6ddd0)"></div>
    <h4>BLOG 3</h4>
    <div class="card-meta"><span>▦ 19.6.2018</span><span>▢ 12 Comments</span></div>
    <p>Lorem Ipsum is simply dummy text of the printing and typesetting industry.</p>
    <span class="more">READ MORE..</span>
  </article>
  <a class="btn" style="left:532px;top:602px;width:136px">View All Blog</a>
</section>

<section class="contact abs">
  <div class="map-shape" role="img" aria-label="Faint world map in the background"></div>
  <h2 class="section-title display" style="top:52px">QUICK CONTACT</h2>
  <div class="title-rule" style="top:110px"></div>
  <div class="field" style="top:178px">Full Name</div>
  <div class="field" style="top:241px">Email Address</div>
  <div class="field" style="top:309px">Massage</div>
  <a class="btn" style="left:532px;top:388px;width:136px">View All Blog</a>
</section>

<footer class="footer abs">
  <h5 style="left:195px;top:44px;font-size:22px;font-weight:500">TEATRO LUNAVERDE</h5>
  <div class="txt" style="left:195px;top:84px;width:230px">Lorem Ipsum is simply dummy text of the printing and typesetting industry.</div>
  <div class="txt" style="left:195px;top:130px;font-size:9px;font-weight:700">READ MORE..</div>
  <div class="socials"><span></span><span></span><span></span><span></span></div>

  <h5 style="left:480px;top:50px">QUICK LINK</h5>
  <div class="txt" style="left:480px;top:83px;line-height:19px">Home<br>Menu<br>Reservation<br>Blogs<br>Contact</div>

  <h5 style="left:609px;top:50px">QUICK LINK</h5>
  <div class="contact-row" style="top:83px">
    <svg width="12" height="16" viewBox="0 0 12 16"><path d="M6 0a6 6 0 0 1 6 6c0 4-6 10-6 10S0 10 0 6a6 6 0 0 1 6-6z" fill="#5a4fb0"/><circle cx="6" cy="6" r="2" fill="#161616"/></svg>
    <span>12 Lindengracht,<br>Amsterdam 1015 KH</span>
  </div>
  <div class="contact-row" style="top:128px">
    <svg width="12" height="14" viewBox="0 0 12 14"><path d="M2 0h3l1 4-2 1a8 8 0 0 0 4 4l1-2 3 1v3c0 1-1 2-2 2C5 13 0 8 0 2c0-1 1-2 2-2z" fill="#5a4fb0"/></svg>
    <span>+31-20-555-0147</span>
  </div>
  <div class="contact-row" style="top:158px">
    <svg width="14" height="10" viewBox="0 0 14 10"><rect width="14" height="10" fill="#5a4fb0"/><path d="M0 0l7 6 7-6" fill="none" stroke="#161616"/></svg>
    <span>hello@teatrolunaverde.example</span>
  </div>

  <h5 style="left:807px;top:50px">SUBSCRIBE</h5>
  <div class="txt" style="left:807px;top:83px;width:215px">Lorem Ipsum is simply dummy text of the printing and typesetting industry.</div>
  <div class="subscribe">Email Address</div>
  <svg class="subscribe-go" viewBox="0 0 49 28"><rect width="49" height="28" fill="#4c4296"/><path d="M17 14l16-7-5 15-3-6z" fill="#fff"/></svg>

  <div class="foot-rule"></div>
  <div class="legal" style="left:195px">© Copyright 2018 Italian Resturent - All Right Reserved</div>
  <div class="legal" style="left:827px">Privacy Policy - Terms &amp; conditions</div>
</footer>

</body>
</html>
```